Delicious premium snack packaging

Background - I have a current range of cakes and cookies that are premium and have a minimalist design style with luxury finish. Feminine and soft touch.

I am looking to create a more affordable but high quality range of packaging for a new product - chocolate Cacao Shards. Whilst keeping the brand essence of ethical luxury but affordable.

Front of the pack - I would like to improve on it and perhaps have a drawing of it that looks enticing to eat than the current. I am open to using product images as well. The current design does not suit retail supermarket shelves.

The back of the pack - I would like to have a nicer organised look that fits the product and brand image. Something more readable and easy to understand that will entice people and educate at the same time. I have a draft which will be attached.

The link to the current range is https://velu.com.sg/collections/velu-everyday

Ideally I would like to revamp the rest of the packs to the similar format and style of the new version for consistency. Pls propose colour options as well. Keeping in mind the main brand style.

Target Market(s)

People who love chocolate, young Gen Z who care about sustainability , parents of children who are any to eat clean ingredients, vegans

Industry/Entity Type

food, snacking

Font styles to use
Other font styles liked:
• Canva font - glacial indifference

Colors

Designer to choose colors to be used in the design.

Requirements
Must have
• Same family vibes as the premium range of cookies
Nice to have
• Colour tones to match the flavours
Should not have
• No bright neon crazy loud colours or designs

```html
<!DOCTYPE html>
<html lang="en">
<head>
<meta charset="utf-8">
<title>Velu Everyday – Cacao Shards Pack</title>
<link rel="stylesheet" href="https://fonts.googleapis.com/css2?family=Poppins:wght@400;500;700;800&display=swap">
<style>
  :root {
    --backdrop: #959595;
    --pouch-white: #efefef;
    --pouch-shade: #e2e2e2;
    --blush: #d8c5c3;
    --gold: #c8a56b;
    --gold-light: #e3c995;
    --cocoa: #3a2215;
    --ink: #3b3331;
    --brand: #8c3a4d;
    --brownie: #3e3c3e;
  }
  * { margin: 0; padding: 0; box-sizing: border-box; }
  html, body { width: 1200px; height: 800px; overflow: hidden; }
  body {
    background: var(--backdrop);
    font-family: "Poppins", sans-serif;
    position: relative;
  }
  .pack {
    position: absolute;
    left: 392px;
    top: 82px;
    width: 416px;
    height: 650px;
  }
  .pack-shape { position: absolute; inset: 0; }
  .brand-name {
    position: absolute;
    top: 112px;
    width: 100%;
    text-align: center;
    color: var(--brand);
    font-weight: 500;
    line-height: 1.15;
  }
  .brand-name .brand-main { display: block; font-size: 46px; letter-spacing: 4px; }
  .brand-name .brand-sub { display: block; font-size: 18px; letter-spacing: 7px; }
  .product-photo {
    position: absolute;
    left: 146px;
    top: 262px;
    width: 124px;
    height: 98px;
  }
  .product-name {
    position: absolute;
    top: 376px;
    width: 100%;
    text-align: center;
    color: var(--cocoa);
    font-weight: 800;
    font-size: 16px;
    line-height: 1.05;
    letter-spacing: 1.5px;
  }
  .divider {
    position: absolute;
    top: 423px;
    left: 168px;
    width: 80px;
    height: 1px;
    background: linear-gradient(90deg, transparent, var(--gold), transparent);
  }
  .tagline {
    position: absolute;
    top: 429px;
    width: 100%;
    text-align: center;
    color: var(--ink);
    font-size: 10.5px;
    line-height: 1.3;
  }
  .claims {
    position: absolute;
    top: 536px;
    left: 0;
    width: 100%;
    display: flex;
    justify-content: center;
    gap: 22px;
    list-style: none;
  }
  .claim { width: 34px; height: 40px; }
  .claim svg { width: 34px; height: 40px; display: block; }
  .net-weight {
    position: absolute;
    top: 596px;
    width: 100%;
    text-align: center;
    color: var(--cocoa);
    font-size: 8px;
    letter-spacing: 1px;
    line-height: 1.2;
  }
  .net-weight strong { display: block; font-size: 9px; font-weight: 700; }
</style>
</head>
<body>
  <div class="pack">
    <svg class="pack-shape" viewBox="0 0 416 650" width="416" height="650">
      <defs>
        <clipPath id="pouch-clip">
          <path d="M12 0 H404 Q416 0 416 12 V638 Q416 650 404 650 H12 Q0 650 0 638 V12 Q0 0 12 0 Z"/>
        </clipPath>
        <linearGradient id="gold-band" x1="0" x2="1">
          <stop offset="0" stop-color="#c8a56b"/>
          <stop offset="0.5" stop-color="#e3c995"/>
          <stop offset="1" stop-color="#c8a56b"/>
        </linearGradient>
      </defs>
      <g clip-path="url(#pouch-clip)">
        <rect class="pouch-body" width="416" height="650" fill="var(--pouch-white)"/>
        <rect class="top-seal" width="416" height="70" fill="var(--pouch-shade)" opacity="0.5"/>
        <line class="zip-line" x1="18" y1="70" x2="398" y2="70" stroke="#d6d6d6" stroke-width="2"/>
        <line class="zip-line" x1="18" y1="84" x2="398" y2="84" stroke="#d6d6d6" stroke-width="2"/>
        <path class="base-panel" d="M0 482 C90 462 170 480 250 505 C320 526 370 520 416 505 V650 H0 Z" fill="var(--blush)"/>
        <path class="gold-wave" d="M0 482 C90 462 170 480 250 505 C320 526 370 520 416 505" fill="none" stroke="url(#gold-band)" stroke-width="5"/>
      </g>
    </svg>

    <h1 class="brand-name"><span class="brand-main">VELU</span><span class="brand-sub">EVERYDAY</span></h1>

    <svg class="product-photo" viewBox="0 0 124 98" role="img" aria-label="Photo of a dark chocolate snack shard studded with seeds">
      <path d="M34 12 L52 10 L70 2 L88 6 L96 24 L118 40 L122 66 L104 82 L84 86 L70 96 L54 84 L30 76 L6 70 L2 54 L20 34 Z" fill="var(--brownie)"/>
    </svg>

    <h2 class="product-name">CACAO<br>SHARDS</h2>
    <div class="divider"></div>
    <p class="tagline">Deeply Chocolatey,<br>from Honest Ingredients</p>

    <ul class="claims">
      <li class="claim">
        <svg viewBox="0 0 34 40" aria-label="vegan">
          <circle cx="17" cy="17" r="16" fill="none" stroke="var(--cocoa)" stroke-width="1.2"/>
          <path d="M9 14 Q9 22 17 24 Q16 17 9 14 Z M25 12 Q25 22 17 24 Q17 15 25 12 Z" fill="var(--cocoa)"/>
          <text x="17" y="39" font-size="5" text-anchor="middle" fill="var(--cocoa)" font-family="Poppins, sans-serif">vegan</text>
        </svg>
      </li>
      <li class="claim">
        <svg viewBox="0 0 34 40" aria-label="no gluten">
          <circle cx="17" cy="17" r="16" fill="none" stroke="var(--cocoa)" stroke-width="1.2"/>
          <line x1="17" y1="9" x2="17" y2="27" stroke="var(--cocoa)" stroke-width="1.4"/>
          <ellipse cx="13.5" cy="14" rx="3" ry="1.8" fill="var(--cocoa)"/>
          <ellipse cx="20.5" cy="14" rx="3" ry="1.8" fill="var(--cocoa)"/>
          <ellipse cx="13.5" cy="19" rx="3" ry="1.8" fill="var(--cocoa)"/>
          <ellipse cx="20.5" cy="19" rx="3" ry="1.8" fill="var(--cocoa)"/>
          <line x1="5" y1="28" x2="29" y2="6" stroke="var(--cocoa)" stroke-width="1.2"/>
          <text x="17" y="39" font-size="5" text-anchor="middle" fill="var(--cocoa)" font-family="Poppins, sans-serif">no gluten</text>
        </svg>
      </li>
      <li class="claim">
        <svg viewBox="0 0 34 40" aria-label="no soy">
          <circle cx="17" cy="17" r="16" fill="none" stroke="var(--cocoa)" stroke-width="1.2"/>
          <rect x="13" y="7" width="8" height="20" rx="4" fill="none" stroke="var(--cocoa)" stroke-width="1.4"/>
          <circle cx="17" cy="12" r="2" fill="var(--cocoa)"/>
          <circle cx="17" cy="17" r="2" fill="var(--cocoa)"/>
          <circle cx="17" cy="22" r="2" fill="var(--cocoa)"/>
          <line x1="5" y1="28" x2="29" y2="6" stroke="var(--cocoa)" stroke-width="1.2"/>
          <text x="17" y="39" font-size="5" text-anchor="middle" fill="var(--cocoa)" font-family="Poppins, sans-serif">no soy</text>
        </svg>
      </li>
      <li class="claim">
        <svg viewBox="0 0 34 40" aria-label="no nuts">
          <circle cx="17" cy="17" r="16" fill="none" stroke="var(--cocoa)" stroke-width="1.2"/>
          <ellipse cx="18" cy="13" rx="6" ry="3.5" fill="none" stroke="var(--cocoa)" stroke-width="1.4"/>
          <ellipse cx="15" cy="21" rx="6" ry="3.5" fill="none" stroke="var(--cocoa)" stroke-width="1.4"/>
          <line x1="5" y1="28" x2="29" y2="6" stroke="var(--cocoa)" stroke-width="1.2"/>
          <text x="17" y="39" font-size="5" text-anchor="middle" fill="var(--cocoa)" font-family="Poppins, sans-serif">no nuts</text>
        </svg>
      </li>
    </ul>

    <p class="net-weight">NET WEIGTH<strong>68g</strong></p>
  </div>
</body>
</html>
```